Need a business letterhead for word docs

Hi, I need a business letterhead. We have had some before but they have issues printing them. I have attached a sample of what we have used that I want improved :) and a PSD of our logo, please use the one with all caps. This will be used for all our correspondance with clients and profeesionals. Our client base are children, so these documents will go to their parents and doctors and paediatricians who also treat these children.

Target Market(s)

Clients (who are families and children) and doctors/paediatricians

Industry/Entity Type

Health Care

Font styles to use
Sans Serif

Colors
85cae6

Requirements
Must have
• My logo and the feel of my logo
Nice to have
• clean feel

```html
<!DOCTYPE html>
<html lang="en">
<head>
<meta charset="utf-8">
<title>Bright Roots Letterhead</title>
<link rel="stylesheet" href="https://fonts.googleapis.com/css2?family=Arimo&family=Nunito+Sans:wght@400;800&display=swap">
<style>
  :root {
    --backdrop: #d9dadb;
    --paper: #f7f7f7;
    --brand-blue: #0b8fc6;
    --brand-light: #85cae6;
    --ink: #111111;
    --muted: #4a4a4a;
    --rule: #c9c9c9;
  }
  * { box-sizing: border-box; margin: 0; padding: 0; }
  html, body { width: 1200px; height: 1200px; overflow: hidden; }
  body {
    background: var(--backdrop);
    display: flex;
    align-items: center;
    justify-content: center;
  }
  .letterhead {
    position: relative;
    width: 806px;
    height: 1140px;
    background: var(--paper);
    box-shadow: 0 6px 24px rgba(0,0,0,0.12);
  }
  .side-band {
    position: absolute;
    top: 0; right: 0;
    width: 54px; height: 100%;
    background: var(--brand-blue);
  }
  .header {
    position: absolute;
    top: 46px; left: 52px; right: 86px;
    display: flex;
    justify-content: space-between;
    align-items: flex-start;
  }
  .brand {
    display: flex;
    align-items: center;
    gap: 12px;
    margin-top: 52px;
  }
  .brand-dot {
    width: 22px; height: 22px;
    border-radius: 50%;
    background: var(--brand-light);
  }
  .brand-name {
    font-family: "Nunito Sans", sans-serif;
    font-weight: 800;
    font-size: 31px;
    letter-spacing: 0.5px;
    color: var(--brand-blue);
  }
  .contact {
    font-family: "Nunito Sans", sans-serif;
    font-weight: 400;
    font-size: 11.5px;
    line-height: 1.25;
    color: var(--muted);
    margin-top: 44px;
  }
  .contact-row {
    display: flex;
    align-items: flex-start;
    gap: 10px;
    margin-bottom: 7px;
  }
  .contact-row svg { flex: none; margin-top: 1px; }
  .addresses { display: flex; gap: 14px; }
  .addresses .divider { width: 1px; background: var(--rule); }
  .body-copy {
    position: absolute;
    top: 232px; left: 56px; right: 112px;
    font-family: "Arimo", sans-serif;
    font-size: 16px;
    line-height: 1.2;
    color: var(--ink);
  }
  .body-copy p { margin-bottom: 19px; }
</style>
</head>
<body>
  <main class="letterhead">
    <div class="side-band"></div>

    <header class="header">
      <div class="brand">
        <span class="brand-dot"></span>
        <span class="brand-name">BRIGHT ROOTS</span>
      </div>

      <div class="contact">
        <div class="contact-row">
          <svg width="10" height="12" viewBox="0 0 10 12"><path d="M5 0a4 4 0 0 0-4 4c0 3 4 8 4 8s4-5 4-8a4 4 0 0 0-4-4zm0 5.5A1.5 1.5 0 1 1 5 2.5a1.5 1.5 0 0 1 0 3z" fill="var(--brand-blue)"/></svg>
          <div class="addresses">
            <span>48 Linden Grove<br>Northvale 3150</span>
            <span class="divider"></span>
            <span>9 Harlow Street<br>Eastmere 3162</span>
          </div>
        </div>
        <div class="contact-row">
          <svg width="11" height="11" viewBox="0 0 12 12"><circle cx="6" cy="6" r="5.3" fill="none" stroke="var(--brand-blue)" stroke-width="1.2"/><path d="M4 3.5c.4 2 1.8 3.6 3.9 4.6l.8-.9" fill="none" stroke="var(--brand-blue)" stroke-width="1.2"/></svg>
          <span>03 9000 4127</span>
        </div>
        <div class="contact-row">
          <svg width="11" height="9" viewBox="0 0 11 9"><rect x="0" y="0" width="11" height="9" rx="1" fill="var(--brand-blue)"/><path d="M0.5 1l5 4 5-4" fill="none" stroke="#ffffff" stroke-width="1"/></svg>
          <span>info@brightrootsclinic.co.au</span>
        </div>
        <div class="contact-row">
          <svg width="11" height="11" viewBox="0 0 12 12"><circle cx="6" cy="6" r="5.3" fill="none" stroke="var(--brand-blue)" stroke-width="1.2"/><ellipse cx="6" cy="6" rx="2.3" ry="5.3" fill="none" stroke="var(--brand-blue)" stroke-width="1"/><path d="M0.7 6h10.6" stroke="var(--brand-blue)" stroke-width="1"/></svg>
          <span>www.brightrootsclinic.com.au</span>
        </div>
      </div>
    </header>

    <section class="body-copy">
      <p>Lorem ipsum dolor sit amet, consectetur adipiscing elit. Nunc a nunc ex. Integer luctus nisi orci, eu aliquam dolor feugiat quis. Suspendisse cursus erat sem, id rutrum tellus venenatis facilisis. Praesent cursus dignissim orci a bibendum. Vestibulum bibendum quam sed lacinia rutrum. Quisque tincidunt ex eu finibus vulputate. In varius pharetra faucibus. Aenean cursus dapibus neque eu fringilla. Vivamus consequat quam vel dolor varius placerat. Pellentesque habitant morbi tristique senectus et netus et malesuada fames ac turpis egestas. Quisque vitae nunc rhoncus, sodales lacus feugiat, fringilla metus. Ut purus lorem, luctus ut mi ut, lobortis vestibulum mi. Nulla facilisi. Donec et pellentesque lacus, et sagittis ex.</p>
      <p>Vestibulum porta risus vitae pellentesque hendrerit. Vestibulum interdum dignissim tellus eu dignissim. Praesent tincidunt varius arcu, ac consequat eros fermentum at. Suspendisse facilisis a tellus ut viverra. Aliquam tincidunt erat quis lectus tristique porta. Maecenas a elementum turpis, in facilisis eros. Sed fermentum purus nisi, quis bibendum nisl volutpat et.</p>
      <p>Nunc maximus feugiat augue, et mattis erat mattis vitae. Nunc et arcu magna. Cras laoreet cursus feugiat. Duis vitae libero et lorem hendrerit porta. Donec mattis risus nec felis rhoncus condimentum. Class aptent taciti sociosqu ad litora torquent per conubia nostra, per inceptos himenaeos. Morbi sed finibus metus, vitae imperdiet nisi.</p>
    </section>
  </main>
</body>
</html>
```